KEB Lau Sound business package.
business cards, stationary, letterhead, envelopes, CD labels and packaging, appointment cards, etc..
Thank you Mr. harven47 !!!!!
CONGRATS 7pixelcrafter
CONGRATS Mr. 7pc!!!!!!!!!!!!!!!!!!
I chose draft #56 as the winner.
I wanted to thank all designers for their great contributions and all your help and great advice.
You guys are all awesome.
I of course wanted to thank Mr. 7pc in particular from the bottom of my heart for always dealing so gracefully and friendly with my sometimes tough to deal with "Mr. Perfectionist" attitude and way of doing things. haha :)
I am super happy with the chosen design.
Fantastic work.
THANK YOU.
Much love to you and your family.
Talor.
@ PH Thank you for your honesty and candor about your likely early decision on the design. I hope all PH's can be as honest and thoughtful. Good luck with your business!!!
It looks like Mr. 7pixelcrafter's draft #48 is going to be the winner.
I know I could always be surprised of course, but I don't think anybody is going to be able to change my mind and beat how I feel about his design.
I know I still have over a day left before this project closes, but... I am only posting this here because I care about your time, talent and energy, and I want to make sure you don't spend extra time and resources on this project if you could be working on other projects where you have a higher likelihood of winning the project.
I am super anxious to see Mr. 7pixelcrafter's revisions I asked for.
My favorite designs btw are:
#20 (all the design AND the business cards), #31 (but not the business cards and not the shirts), #37 and #38
It looks like this is going to go between Mr. 7pixelcrafter and my friend who created the logo Mr. Harven47 for the winning bid.
We seem to have an India vs. India house contest here haha.
At this time: I tend to lean over to really liking #20 and #31 as my favorites.
Tips and pointers:
1) I gravitate towards preferring having the contact info at the bottom of the fax/letterhead (as in #20 and #31)
I have a feeling that the design that is going to win, is going to be the design that has the contact info at the bottom, and the company name more featured on top of the letterhead/fax design.
2) I prefer ligher colors that fit/match as closely as possible to the color of the KEB Lau Sound logo.
3) I tend to prefer having the KEB Lau Sound logo featured.. meaning: larger... on business cards, letterheads, fax pages, actually... everything.
4) I tend to lean towards liking having the big "O" with headphones logo on the lower left corner of fax/letterhead pages as a light background/watermark
5) I REALLY really like it when ALL materials have a certain design element that ties ALL materials together. Which is why I for example REALLY like #20 (ALL the materials have exactly the same design elements
6) I would LOOOOOVEEE to see copies/drafts of my 4 favorite designs mentioned above, with some slight touch of silver added to the white backgrounds of all materials/stationary. (As in the silver-ish kind of background in the original "white/silver background" of the KEB Lau Sound logo file I uploaded for this project)
Fixes:
1) I need to have the 415-738-2261 (cell) number on top of the landline (323 etc) number on all materials. (cell first)
2) I absolutely want the center of the O's in "KEB Lau Sound" to be exactly the same color as the background (on ALL materials). If the background is black, I want the center of the O to be black as well, if it is turquoise, then I want the center of the O to be turquoise as well, etc... etc...
Thank you for all your amazing work.
Much respect and love for all your work and your talent.
Best
First off:
I am SUPER HAPPY with all your submissions. You are ALL doing an amazing job and it is again going to be very hard for me to choose here. :)
So here's some guidance, sharing with you my favorite things I have seen, likes, etc...
Right now my 2 favorite ones are #33 and #31
My favorite color so far is Mr. Harven's #33
Mr Harven, Could I see a copy of the fax sheet and stationary/letterhead with the big O in the lower left corner
1) much lighter in color (kind a like a watermark. My concern is that it might interfere with typed text on the letter as it is now)
2) with that big O moved a bit to the left so the whole symbol is on the page.
3) with the company name/logo bigger on all materials.
(This does not have to be 3 different drafts btw... trying to save you time here... I am looking for one draft that has all these 3 things all together.)
More about #33
I LOVE the simplicity of the footer (bottom of page) you created on the letterhead/footer and fax page.
On the business cards: you did an amazing job on the color of the back of the business card. Keep it that way please haha. However: you know how much I am in love with color of the logo you created: is there any way you can have the logo/business name in the original color (instead of white) on that awesome background you created here?? (not sure if that would work, or if it would be too much of the same color?)
How would it look like if you made the word 'Music" black?
Mr. 7pixelcrafter draft #31
I completely LOVE how you did this smart out of the box thinking thing and made the business cards vertical (which is pretty unusual haha). So cool.
I also really frigging like what you did with the blue hue color lettering in my name and URL on the business cards.
I also adore the design of the fax sheet and letterhead. I really like it's simplicity.
But can I see a draft of the letterhead and fax page: where
1) you make a the company logo top left corner a bit bigger
2) Can you also add the O with head phones in the lower right corner, very lightly (like a watermark type thing)
Lastly: I am trying to figure out how I like the business cards with the company name in the big O.
Part of me is in love with the company logo design, and want to see it bigger and free (meaning: not surrounded by the big O ). I prefer the idea of using that O icon as a lighter background/watermark kind a thing.
Comments for everybody:
1) I need to have my cell phone number and email on the CD labels and on the CD insert sheet.
2) I would like you all to use little icons instead of using the words "cell", "address", "phone", etc...
The reason being that icons are more international: the word "cell" for example in Britain or Australia is confusing, as they call it a "mobile" there.
3) Us a little "house" icon for "address"
4) I want my cell number, to be ABOVE my land line/phone number
5) I want the address LAST. (Think about it: people have short attention spans haha... it's all about marketing and grabbing people... the FIRST thing they want to see is where to get in touch with you right now... your cell phone... not where you live.)
Draft #26 and #27
I like your very smart idea of creating tablature paper, music paper etc... with my logo and business name/logo on. You get extra points sir for that amazing idea. I should have thought of that myself already, but you beat me to it haha.
On the black shirt: I would not put the O logo on the front, as it makes it a bit too heavy and busy, already having my name logo there. I woud make the name logo bigger, and have the big O on the back of the shirt. Also: no tilted O.
On the white top: FANTASTIC artwork with the O logo... I really like the dotted approach you came up with here.
I also like how you picked up on my asking in an earlier post about the more silvery approach I wanted to see examples of.

```html
<!DOCTYPE html>
<html lang="en">
<head>
<meta charset="utf-8">
<title>KEB Lau Sound — Stationery Package</title>
<link href="https://fonts.googleapis.com/css2?family=Arimo:wght@400;700&display=swap" rel="stylesheet">
<style>
  :root{
    --stage:#2e2f31;
    --paper:#ffffff;
    --silver:#e9eef2;
    --blue:#1b8fd6;
    --blue-deep:#0f6fb3;
    --blue-light:#67bff0;
    --blue-pale:#cde9f8;
    --ink:#2d3a44;
    --muted:#7c8a94;
  }
  *{box-sizing:border-box;margin:0;padding:0}
  html,body{width:1200px;height:871px;overflow:hidden}
  body{background:var(--stage);font-family:"Arimo",Arial,sans-serif;color:var(--ink);position:relative}
  .piece{position:absolute;overflow:hidden;box-shadow:0 4px 14px rgba(0,0,0,.45)}
  .wave{position:absolute;left:0;bottom:0;width:100%}
  .wordmark{font-weight:700;color:var(--blue);letter-spacing:-.5px;display:flex;align-items:center;gap:6px;white-space:nowrap}
  .wordmark .dot{border-radius:50%;background:var(--blue);flex:none}
  .soft-art{position:absolute}

  /* business card back */
  .card-back{left:80px;top:60px;width:140px;height:96px;border-radius:8px;
    background:radial-gradient(circle at 50% 45%,var(--blue-light),var(--blue) 70%)}
  .card-back .mark{position:absolute;left:50%;top:44%;transform:translate(-50%,-50%);width:38px;height:38px;border-radius:50%;background:var(--paper)}
  .card-back .url{position:absolute;bottom:9px;width:100%;text-align:center;color:#fff;font-size:5px}

  /* business card front */
  .card-front{left:235px;top:28px;width:150px;height:110px;border-radius:8px;background:linear-gradient(180deg,#fff,var(--silver))}
  .card-front .name{position:absolute;left:10px;top:10px;font-size:6.5px;font-weight:700;color:var(--blue-deep)}
  .card-front .role{position:absolute;left:10px;top:19px;font-size:4.5px;color:var(--muted)}
  .card-front .lines{position:absolute;left:10px;top:34px;font-size:4.5px;line-height:6.5px;color:var(--ink)}
  .card-front .url{position:absolute;left:10px;bottom:24px;font-size:5px;font-weight:700;color:var(--blue)}

  /* letterhead & fax */
  .sheet{width:250px;height:372px;background:linear-gradient(180deg,#fff 55%,var(--silver))}
  .letterhead{left:40px;top:210px}
  .fax{left:310px;top:210px}
  .sheet .wordmark{position:absolute;left:16px;top:20px;font-size:19px}
  .sheet .wordmark .dot{width:10px;height:10px}
  .sheet .rule{position:absolute;left:16px;right:16px;top:50px;height:2px;background:linear-gradient(90deg,var(--blue),transparent)}
  .sheet .foot{position:absolute;left:14px;bottom:10px;color:#fff;font-size:5.5px;line-height:7.5px}
  .sheet .foot-url{position:absolute;right:14px;bottom:10px;color:#fff;font-size:5.5px}
  .fax-title{position:absolute;left:16px;top:62px;font-size:24px;font-weight:700;color:var(--blue)}
  .fax-fields{position:absolute;left:16px;right:16px;top:98px;display:grid;grid-template-columns:1fr 1fr;column-gap:14px;row-gap:9px}
  .fax-fields span{font-size:8px;font-weight:700;color:var(--blue-deep);border-bottom:1px solid var(--blue-pale);padding-bottom:3px}
  .fax-checks{position:absolute;left:16px;top:210px;font-size:8px;font-weight:700;color:var(--blue-deep);line-height:15px}
  .fax-checks i{display:inline-block;width:8px;height:8px;border:1px solid var(--blue);margin-right:5px;vertical-align:-1px}
  .fax-comments{position:absolute;left:16px;top:250px;font-size:8px;font-weight:700;color:var(--blue-deep)}

  /* CD */
  .cd{left:620px;top:22px;width:168px;height:168px;border-radius:50%;
    background:radial-gradient(circle,var(--blue-light) 0,var(--blue) 55%,var(--blue-deep) 100%)}
  .cd .hub{position:absolute;left:50%;top:50%;width:40px;height:40px;margin:-20px 0 0 -20px;border-radius:50%;background:var(--paper);border:6px solid var(--blue-pale)}
  .cd .wordmark{position:absolute;left:50%;top:112px;transform:translateX(-50%);font-size:13px;color:#fff}
  .cd .tag{position:absolute;left:50%;top:12px;transform:translateX(-50%);font-size:5px;color:#fff}

  /* CD sleeve */
  .sleeve{left:600px;top:210px;width:200px;height:150px;background:linear-gradient(180deg,#fff,var(--silver))}
  .sleeve .flap{position:absolute;left:0;top:0;width:100%}
  .sleeve .ring{position:absolute;left:118px;top:22px;width:64px;height:64px;border-radius:50%;border:2px solid var(--blue-pale)}

  /* envelope */
  .envelope{left:700px;top:560px;width:470px;height:230px;background:linear-gradient(180deg,#fff,var(--silver))}
  .envelope .band{position:absolute;left:0;top:0;width:100%;height:40px}
  .envelope .band-text{position:absolute;top:14px;width:100%;text-align:center;font-size:6px;color:var(--muted)}
  .envelope .wordmark{position:absolute;left:28px;top:92px;font-size:34px}
  .envelope .wordmark .dot{width:16px;height:16px}
  .envelope .url{position:absolute;left:30px;top:140px;font-size:7px;color:var(--muted)}
  .envelope .addr{position:absolute;right:26px;bottom:26px;font-size:7px;line-height:10px;color:#fff;text-align:left}
</style>
</head>
<body>

<!-- Business card back -->
<div class="piece card-back">
  <div class="mark"></div>
  <div class="url">www.keblausound.com</div>
</div>

<!-- Business card front -->
<div class="piece card-front">
  <div class="name">Talor R. Marwick</div>
  <div class="role">Producer &amp; Sound Engineer</div>
  <div class="lines">P.O. Box 5127<br>Glendale, CA 91209<br>415-738-2261<br>323-555-0147</div>
  <div class="url">www.keblausound.com</div>
  <svg class="wave" viewBox="0 0 150 22" height="22" preserveAspectRatio="none"><path d="M0 10 Q60 0 150 6 V22 H0Z" fill="var(--blue)"/></svg>
</div>

<!-- Letterhead -->
<div class="piece sheet letterhead">
  <div class="wordmark"><span class="dot"></span>KEB Lau Sound</div>
  <div class="rule"></div>
  <div class="soft-art" role="img" aria-label="Faint brand watermark and star cluster" style="left:40px;bottom:40px;width:190px;height:130px;border-radius:50%;background:radial-gradient(circle,rgba(27,143,214,.12),transparent 70%)"></div>
  <svg class="wave" viewBox="0 0 250 50" height="50" preserveAspectRatio="none"><path d="M0 18 Q120 2 250 12 V50 H0Z" fill="var(--blue)"/></svg>
  <div class="foot">P.O. Box 5127<br>Glendale, CA 91209 · USA<br>415-738-2261 · 323-555-0147</div>
  <div class="foot-url">www.keblausound.com</div>
</div>

<!-- Fax -->
<div class="piece sheet fax">
  <div class="wordmark"><span class="dot"></span>KEB Lau Sound</div>
  <div class="rule"></div>
  <div class="fax-title">FAX</div>
  <div class="fax-fields">
    <span>To:</span><span>From:</span>
    <span>Fax:</span><span>Pages:</span>
    <span>Phone:</span><span>Date:</span>
    <span>Re:</span><span>Cc:</span>
  </div>
  <div class="fax-checks"><i></i>Urgent<br><i></i>Please reply</div>
  <div class="fax-comments">Comments :</div>
  <div class="soft-art" role="img" aria-label="Faint brand watermark and star cluster" style="left:90px;bottom:40px;width:170px;height:140px;border-radius:50%;background:radial-gradient(circle,rgba(27,143,214,.14),transparent 70%)"></div>
  <svg class="wave" viewBox="0 0 250 50" height="50" preserveAspectRatio="none"><path d="M0 18 Q120 2 250 12 V50 H0Z" fill="var(--blue)"/></svg>
  <div class="foot">P.O. Box 5127 · Glendale, CA 91209<br>415-738-2261 · 323-555-0147</div>
  <div class="foot-url">www.keblausound.com</div>
</div>

<!-- CD label -->
<div class="piece cd">
  <div class="tag">info@keblausound.com</div>
  <div class="hub"></div>
  <div class="wordmark">KEB Lau Sound</div>
</div>

<!-- CD sleeve -->
<div class="piece sleeve">
  <svg class="flap" viewBox="0 0 200 30" height="30" preserveAspectRatio="none"><path d="M0 0 H200 V8 Q100 30 0 8Z" fill="var(--blue-pale)"/></svg>
  <div class="ring"></div>
  <svg class="wave" viewBox="0 0 200 40" height="40" preserveAspectRatio="none"><path d="M0 16 Q100 0 200 10 V40 H0Z" fill="var(--blue)"/></svg>
</div>

<!-- Envelope -->
<div class="piece envelope">
  <svg class="band" viewBox="0 0 470 40" preserveAspectRatio="none"><path d="M0 0 H470 V26 Q235 42 0 26Z" fill="var(--silver)"/><path d="M0 26 Q235 42 470 26" stroke="var(--blue)" stroke-width="2" fill="none"/></svg>
  <div class="band-text">Your sound, our passion</div>
  <div class="wordmark"><span class="dot"></span>KEB Lau Sound</div>
  <div class="url">www.keblausound.com</div>
  <div class="soft-art" role="img" aria-label="Star cluster decoration" style="right:20px;top:70px;width:90px;height:60px;border-radius:50%;background:radial-gradient(circle,rgba(27,143,214,.25),transparent 70%)"></div>
  <svg class="wave" viewBox="0 0 470 70" height="70" preserveAspectRatio="none"><path d="M0 30 Q230 0 470 22 V70 H0Z" fill="var(--blue)"/></svg>
  <div class="addr">P.O. Box 5127<br>Glendale, CA 91209<br>415-738-2261 · 323-555-0147</div>
</div>

</body>
</html>
```